Business Card Design Project

parking lot sealing and striping company

Industry/Entity Type

Business

Contact Information for Business Card

See pics below, blue and gray colors

```html
<!DOCTYPE html>
<html lang="en">
<head>
<meta charset="utf-8">
<title>Tarline Asphalt Sealings – Business Card</title>
<link rel="stylesheet" href="https://fonts.googleapis.com/css2?family=Jost:ital,wght@0,400;0,700;1,300&family=Roboto:ital,wght@0,400;0,500;1,400&family=Fredoka:wght@600&display=swap">
<style>
  :root {
    --stage: #1b1d21;
    --card: #dcdbe0;
    --deep-blue: #1566c2;
    --sky-blue: #1d9fe0;
    --frost: #e4f1fa;
    --navy: #1b2a4a;
    --ink: #222226;
    --link: #1ba9d3;
  }
  * { box-sizing: border-box; margin: 0; padding: 0; }
  html, body {
    width: 1200px; height: 950px; overflow: hidden;
    background: var(--stage);
  }
  .card {
    position: absolute; left: 42px; top: 140px;
    width: 1063px; height: 638px;
    background: var(--card);
    overflow: hidden;
    transform: scale(1.05); transform-origin: top left;
  }
  .card-waves { position: absolute; inset: 0; width: 1063px; height: 638px; }
  .brand {
    position: absolute; left: 528px; top: 82px;
    display: flex; align-items: center; gap: 34px;
  }
  .brand-square {
    width: 103px; height: 81px; background: var(--sky-blue);
  }
  .brand-name {
    font-family: "Jost", sans-serif; font-weight: 700; color: var(--navy);
    line-height: 1;
  }
  .brand-name .word { display: block; font-size: 48px; letter-spacing: 5px; }
  .brand-name .trade { display: block; font-size: 22px; letter-spacing: 5.5px; margin-top: 10px; }
  .tagline {
    position: absolute; left: 530px; top: 172px; width: 458px;
    font-family: "Fredoka", sans-serif; font-weight: 600;
    font-size: 27px; letter-spacing: 1.3px; color: var(--navy);
    white-space: nowrap;
  }
  .contact {
    position: absolute; right: 85px; top: 266px; text-align: right;
  }
  .contact-name {
    font-family: "Jost", sans-serif; font-style: italic; font-weight: 300;
    font-size: 40px; color: var(--ink); letter-spacing: 0.5px; line-height: 1.1;
  }
  .contact-phone {
    font-family: "Roboto", sans-serif; font-size: 22px; color: var(--ink);
    margin-top: 4px;
  }
  .contact-web {
    font-family: "Roboto", sans-serif; font-style: italic;
    font-size: 25px; color: var(--link); letter-spacing: 0.6px; margin-top: 4px;
  }
  .services {
    position: absolute; left: 364px; top: 432px; width: 640px;
    font-family: "Roboto", sans-serif; font-weight: 500;
    font-size: 20px; line-height: 31.5px; color: var(--ink); letter-spacing: 0.3px;
  }
  .services .tail { padding-left: 6px; }
</style>
</head>
<body>
  <div class="card">
    <svg class="card-waves" viewBox="0 0 1063 638" aria-hidden="true">
      <path d="M0,0 L390,0 C230,120 200,470 480,638 L0,638 Z" fill="var(--deep-blue)"/>
      <path d="M250,0 L390,0 C230,120 205,460 370,570 C180,450 170,120 250,0 Z" fill="var(--sky-blue)"/>
      <path d="M257,0 C168,130 178,440 370,570" fill="none" stroke="var(--card)" stroke-width="8"/>
      <path d="M168,155 C130,330 200,540 430,638 L385,638 C230,560 152,380 168,155 Z" fill="var(--frost)"/>
    </svg>

    <div class="brand">
      <div class="brand-square"></div>
      <div class="brand-name">
        <span class="word">TARLINE</span>
        <span class="trade">ASPHALT SEALINGS</span>
      </div>
    </div>
    <div class="tagline">SPEND A LITTLE TO SAVE A LOT</div>

    <div class="contact">
      <div class="contact-name">MARCUS DELANEY</div>
      <div class="contact-phone">PHONE:555.010.2468</div>
      <div class="contact-web">info@tarline.com &nbsp;|&nbsp; www.tarline.com</div>
    </div>

    <div class="services">
      ASPHALT SEALING &nbsp;|&nbsp; CRACK REPAIR &nbsp;|&nbsp; RAMP BUILDING<br>
      LINE PAINTING &nbsp;|&nbsp; CONCRETE CURE &nbsp;|&nbsp; WALKWAY SEALING<br>
      OIL STAIN REMOVAL &nbsp;|&nbsp; PARKING LOT CLEANUP &nbsp;|&nbsp; POTHOLE<br>
      <span class="tail">AND GAP FILLING</span>
    </div>
  </div>
</body>
</html>
```